MaplePilot Dating Plattform Design Proposal

Layout Proposal
HTML or PSD

Dating Platform, where young ladies (f.e. students) are looking for generous man that support them. In return they will spend time with the sugar daddies (dining, cinema, exhibitions, romantic rendez-vous).

Page consist out of 2 pages
1. Primary landing page
2. Detail page for each profile

1. Primary Landing Page
a. Headline: Hier suchen JUNGE FRAUEN, den REIFEN MANN der weiss wie zu verwöhnen!
b. Subtitle/Explanation (can be positioned on top of profiles or at side): Viele junge Frauen können nichts mit den Männern in ihrem Alter anfangen oder sie lieben einfach die Möglichkeiten die ihnen ein reiferer Mann bieten kann. Auf Mapplepilot bieten wir den jungen Damen dafür eine Kontaktmöglichkeit. Sie inserieren auf Maplpilot privat und sind keine profesionellen.
c. List of Profiles with pictures, description text, name and number
2. Detail Page
a. Picture of Profile
b. Description Text
c. Additional blurred pictures
d. Field to enter email to see pictures unblurred

Example pages:
- http://nachtfalter-plauschwelt.ch/

Design:
- Feel free for your suggestions of look’n’feel. Keep in mind that we address generous man
- The way how profiles (20 -30 total) shall be listed on Page 1 is up to you (list, carroussel, slider,..)
- As well feel free to add any background pics/aminations

Attached find Excel with profiles and ZIP with pictures

Dating

2 page

• Page consist out of 2 pages
• 1. Primary landing page
• 2. Detail page for each profile
• 1. Primary Landing Page
• a. Headline: Hier suchen JUNGE FRAUEN, den REIFEN MANN der weiss wie zu verwöhnen!
• b. Subtitle/Explanation (can be positioned on top of profiles or at side): Viele junge Frauen können nichts mit den Männern in ihrem Alter anfangen oder sie lieben einfach die Möglichkeiten die ihnen ein reiferer Mann bieten kann. Auf Mapplepilot bieten wir den jungen Damen dafür eine Kontaktmöglichkeit. Sie inserieren auf Maplpilot privat und sind keine profesionellen.
• c. List of Profiles with pictures, description text, name and number
• 2. Detail Page
• a. Picture of Profile
• b. Description Text
• c. Additional blurred pictures
• d. Field to enter email to see pictures unblurred

```html
<!DOCTYPE html>
<html lang="de">
<head>
<meta charset="utf-8">
<title>MaplePilot Dating</title>
<link href="https://fonts.googleapis.com/css2?family=Open+Sans:wght@400;600;700&family=Oswald:wght@500&family=Arvo:wght@400;700&family=Arimo:wght@400;700&display=swap" rel="stylesheet">
<style>
:root{
  --pink:#e8237f;
  --pink-dark:#d01a6f;
  --bar:#232323;
  --hero-dark:#1d1a1b;
  --band:#e5287f;
  --text:#333;
  --card-bg:#fff;
  --card-tint:#fbe4ef;
  --footer:#353535;
  --blue:#1587b5;
}
*{box-sizing:border-box;margin:0;padding:0}
html,body{width:1200px;height:2278px;overflow:hidden}
body{position:relative;font-family:"Open Sans",sans-serif;color:var(--text);background:linear-gradient(#e9e9e9 0,#f4f4f4 900px,#fafafa 1500px,#fff 100%)}

.hero{position:relative;height:592px;color:#fff;text-align:center}
.hero-photo{position:absolute;inset:0;background:radial-gradient(ellipse at 80% 40%,#4a3a3a 0,#2a2223 40%,#141213 100%)}
.topbar{position:relative;height:76px;background:rgba(30,30,30,.85);display:flex;align-items:center;padding:0 100px}
.brand{font-family:"Open Sans",sans-serif;font-weight:700;font-size:30px;color:var(--pink);letter-spacing:-.5px;white-space:nowrap}
.topnav{margin-left:auto;display:flex;align-items:center;gap:22px}
.topnav .search{color:#fff;font-size:13px;text-decoration:none;white-space:nowrap}
.topnav .login{background:var(--pink);color:#fff;font-size:13px;text-decoration:none;padding:0 16px;height:35px;line-height:35px;white-space:nowrap;text-align:center}

.hero-copy{position:relative;padding-top:44px}
.hero-copy .lead{font-size:17px;font-family:"Arimo",sans-serif}
.hero-copy h1{font-family:"Arimo",sans-serif;font-weight:400;font-size:26px;margin-top:10px;letter-spacing:.5px}
.hero-copy h1 b{font-size:36px;font-weight:700}
.hero-copy .tail{font-size:16px;margin-top:12px;font-family:"Arimo",sans-serif}

.signup{position:absolute;left:421px;top:258px;width:358px;height:334px;background:#fff;padding:20px 35px 0;text-align:left;color:#333}
.signup h2{font-family:"Oswald",sans-serif;font-weight:500;color:var(--pink);font-size:36px;text-align:center;line-height:44px;white-space:nowrap}
.signup label{display:block;font-size:12px;margin-top:14px}
.signup .input{margin-top:8px;height:38px;background:#f0f0f0;border:1px solid #e4e4e4;font-size:11px;color:#aaa;padding:11px 9px}
.signup .birthday{display:flex;align-items:center;gap:6px;font-size:12px;margin-top:14px}
.signup .select{border:1px solid #ccc;height:22px;font-size:11px;padding:3px 4px;display:flex;align-items:center;gap:4px}
.signup .select svg{width:6px;height:5px}
.signup .join{margin-top:16px;height:38px;background:linear-gradient(#1994c4,#0f79a6);color:#fff;text-align:center;line-height:38px;font-size:13px}

.intro{height:118px;background:var(--band);color:#fff;font-family:"Arvo",serif;font-size:18.5px;line-height:30px;padding:11px 100px 0}

.profiles{display:flex;gap:17px;padding:35px 0 0 94px}
.col{width:190px;display:flex;flex-direction:column;gap:21px}
.card{background:linear-gradient(#fff 55%,var(--card-tint));box-shadow:0 0 4px rgba(0,0,0,.25);padding:4px 4px 8px}
.photo{position:relative;height:137px}
.badge{position:absolute;right:0;bottom:4px;background:rgba(0,0,0,.65);color:#fff;font-size:11px;padding:3px 7px;display:flex;align-items:center;gap:5px;white-space:nowrap}
.badge svg{width:16px;height:12px}
.name{background:var(--pink);color:#fff;font-family:"Arvo",serif;font-weight:700;font-size:15px;height:27px;line-height:27px;padding-left:6px;margin-top:4px;letter-spacing:.5px}
.desc{font-size:11px;line-height:16px;padding:6px 2px 0;text-align:left}
.phone{display:flex;align-items:center;gap:8px;font-weight:700;font-size:18px;color:#222;padding:10px 2px 0;border-top:1px solid #eee;margin-top:8px;white-space:nowrap}
.phone svg{width:14px;height:14px}

.footer{position:absolute;left:0;right:0;bottom:0;height:98px;background:var(--footer);border-top:3px solid #ccc;display:flex;align-items:center;padding:0 100px;font-size:11px;color:#ddd}
.footer nav{display:flex;gap:26px}
.footer span{white-space:nowrap}
.footer .copy{margin-left:auto}
</style>
</head>
<body>

<header class="hero">
  <div class="hero-photo" role="img" aria-label="Dunkles Stimmungsfoto einer jungen Frau auf einem Sofa"></div>
  <div class="topbar">
    <span class="brand">MaplePilot Dating</span>
    <nav class="topnav"><a class="search" href="#">Search</a><a class="login" href="#">Members login</a></nav>
  </div>
  <div class="hero-copy">
    <p class="lead">Hier suchen</p>
    <h1><b>JUNGE FRAUEN</b>, den <b>REIFEN MANN</b></h1>
    <p class="tail">der weiss wie zu verwöhnen!</p>
  </div>
  <form class="signup">
    <h2>Join Now. It’s FREE</h2>
    <label>Email Address:</label>
    <div class="input">Your email</div>
    <label>Password:</label>
    <div class="input">Your email</div>
    <div class="birthday">Birthday :
      <span class="select">01 <svg viewBox="0 0 6 5"><path d="M0 0h6L3 5z" fill="#555"/></svg></span>
      <span class="select">01 <svg viewBox="0 0 6 5"><path d="M0 0h6L3 5z" fill="#555"/></svg></span>
      <span class="select">1986 <svg viewBox="0 0 6 5"><path d="M0 0h6L3 5z" fill="#555"/></svg></span>
    </div>
    <div class="join">JOIN FREE</div>
  </form>
</header>

<section class="intro">Viele junge Frauen können nichts mit den Männern in ihrem Alter anfangen oder sie lieben einfach die Möglichkeiten die ihnen ein reiferer Mann bieten kann. Auf Mapplepilot bieten wir den jungen Damen dafür eine Kontaktmöglichkeit. Sie inserieren auf Maplpilot privat und sind keine profesionellen.</section>

<svg width="0" height="0" style="position:absolute">
  <symbol id="cam" viewBox="0 0 16 12"><rect x="0" y="3" width="11" height="8" rx="1" fill="#fff"/><path d="M11 6l5-3v8l-5-3z" fill="#fff"/><circle cx="3" cy="1.5" r="1.5" fill="#fff"/><circle cx="7" cy="1.5" r="1.5" fill="#fff"/></symbol>
  <symbol id="tel" viewBox="0 0 14 14"><path d="M3 0l3 3-2 2c1 2 3 4 5 5l2-2 3 3-2 3C6 13 1 8 0 2z" fill="#e8237f"/></symbol>
</svg>

<main class="profiles">
  <div class="col">
    <article class="card">
      <div class="photo" role="img" aria-label="Profilfoto von Becky" style="background:linear-gradient(#6b4a3c,#2e2320)"><span class="badge"><svg><use href="#cam"/></svg></span></div>
      <h3 class="name">BECKY</h3>
      <p class="desc">Bin eine Studentin, mit knappem Taschengeld. Träume von entspannten Abenden bei gutem Essen. Wenn du mir meinen Traum erfüllst, versichere ich dir meine Dankbarkeit. Bitte nicht schüchtern sein, bin der Typ Mädchen von nebenan mit dem man immer eine gute Zeit hat.</p>
      <div class="phone"><svg><use href="#tel"/></svg>0790001122</div>
    </article>
    <article class="card">
      <div class="photo" role="img" aria-label="Profilfoto von Gina" style="background:linear-gradient(#7a6a62,#3a302c)"><span class="badge"><svg><use href="#cam"/></svg>4 Photos</span></div>
      <h3 class="name">GINA</h3>
      <p class="desc">Gina, Model und Künstlerin: Suche einen grosszügigen, aufmerksamen und reiferen Herr, für gelegentliche Altagsfluchten. Mich stört es nicht wenn du ein Bauch hast, wichtig ist mir, dass du mich verwöhnst und wie eine Dame behandelst. Hoffe auf bald, mit dir. Schreib mir bitte bald :*.</p>
      <div class="phone"><svg><use href="#tel"/></svg>0790001122</div>
    </article>
    <article class="card">
      <div class="photo" role="img" aria-label="Profilfoto von Suze" style="background:linear-gradient(#b58a78,#6e4c42)"><span class="badge"><svg><use href="#cam"/></svg>3 Photos</span></div>
      <h3 class="name">SUZE</h3>
      <p class="desc">Tänzerin liebt Tagträume: Was gibt es Schöneres als mit einem gepflegten Herren gemeinsam Champagner zu trinken?! Den gleichaltrigen Männern fehlt dazu der Sinn und die Möglichkeiten. Freue mich über jede Anschrift. Bisou deine Suze</p>
      <div class="phone"><svg><use href="#tel"/></svg>0790001122</div>
    </article>
  </div>

  <div class="col">
    <article class="card">
      <div class="photo" role="img" aria-label="Profilfoto von Brenda" style="background:linear-gradient(#8a6a5c,#2a1f1c)"><span class="badge"><svg><use href="#cam"/></svg>4 Photos</span></div>
      <h3 class="name">BRENDA</h3>
      <p class="desc">Kerzenschein, ein Glas Burgunder und sanfter Jazz im Hintergrund, so stell ich mir einen gelungenen Abend an der Seite eines Mannes vor. Dies kann mir kein Mann in meinem Alter bieten. Ich brauche einen Mann, zu dem ich aufsehen kann. Erotisch und materiell können junge Männer meine Ansprüche oft nicht erfüllen. Freu mich auf deine Nachricht.</p>
      <div class="phone"><svg><use href="#tel"/></svg>0790001122</div>
    </article>
    <article class="card">
      <div class="photo" role="img" aria-label="Profilfoto von Lara" style="background:linear-gradient(#4a4440,#1c1a19)"><span class="badge"><svg><use href="#cam"/></svg>3 Photos</span></div>
      <h3 class="name">LARA</h3>
      <p class="desc">Coifeuse aus Zürich: Habe mich hier angemeldet um Männer kennenzulernen welche schon Lebenserfahrung haben. Mir gefällt es wenn ein Mann einen gewissen Erfahrungsschatz hat und auch weiss wie man eine Dame ausführt und verwöhnt. Freue mich schon auf deine Einladung zum Dinner.</p>
      <div class="phone"><svg><use href="#tel"/></svg>0790001122</div>
    </article>
    <article class="card">
      <div class="photo" role="img" aria-label="Profilfoto von Tanja in Schwarzweiss" style="background:linear-gradient(#9a9a9a,#3a3a3a)"><span class="badge"><svg><use href="#cam"/></svg>4 Photos</span></div>
      <h3 class="name">TANJA</h3>
      <p class="desc">Geschichtsstudentin finanziell unabhängig, träumt von Reisen zu zweit. Bist du der gepflegte Mann, der Freude an einer charmanten, unkomplizierten und offenen Begleitung auf Reisen hat? Ja melde dich bitte bei mir. Können uns bei unserem ersten lockeren Treffen über unsere Reiselust unterhalten.</p>
      <div class="phone"><svg><use href="#tel"/></svg>0790001122</div>
    </article>
  </div>

  <div class="col">
    <article class="card">
      <div class="photo" role="img" aria-label="Profilfoto von Carla" style="background:linear-gradient(#9a4a38,#3a2220)"><span class="badge"><svg><use href="#cam"/></svg>3 Photos</span></div>
      <h3 class="name">CARLA</h3>
      <p class="desc">Heissblütiger Rotschopf sucht: Meine Eltern sind sehr liebevoll, doch auch ein wenig unorganisiert, darum finanziere ich mein Philosophie Studium alleine. Über Eine Prise Luxus abundzu würde ich mich darum sehr dankbar zeigen. Welcher Mann hat ein grosses Herz für eine Studentin. Einfach eine SMS schreiben.</p>
      <div class="phone"><svg><use href="#tel"/></svg>0790001122</div>
    </article>
    <article class="card">
      <div class="photo" role="img" aria-label="Profilfoto von Loraine" style="background:linear-gradient(#8c8680,#4a4440)"><span class="badge"><svg><use href="#cam"/></svg>4 Photos</span></div>
      <h3 class="name">LORAINE</h3>
      <p class="desc">Mein lieber Gentleman, befinde mich momentan in einer Situation, in der ich auf die Hilfe und Unterstützung eines Mannes angewiesen bin. Bist du der diskrete Geniesser, der dafür in Frage kommt? Melde dich :)</p>
      <div class="phone"><svg><use href="#tel"/></svg>0790001122</div>
    </article>
    <article class="card">
      <div class="photo" role="img" aria-label="Profilfoto von Vanja" style="background:linear-gradient(#6a5a58,#2a2424)"><span class="badge"><svg><use href="#cam"/></svg>4 Photos</span></div>
      <h3 class="name">VANJA</h3>
      <p class="desc">Suche ein längerfristiges Arrangement mit einem Herren. Die Beziehung soll von Genuss, Sympathie und gegenseitigem Respekt geprägt sein. Ich habe einen sehr offenen, grosszügigen und geduldigen Charakter und erwarte dasselbe von Dir. Dein Aussehen ist für mich nebensächlich und ich liebe Männer mit Bauch, ist so schön kuschlig. Was mich aber abtörnt ist Geiz. fühlst du dich angesprochen, dann zögere nicht mich zu kontaktieren.</p>
      <div class="phone"><svg><use href="#tel"/></svg>0790001122</div>
    </article>
  </div>

  <div class="col">
    <article class="card">
      <div class="photo" role="img" aria-label="Profilfoto von Celine" style="background:linear-gradient(#8a7a6c,#4a3c34)"><span class="badge"><svg><use href="#cam"/></svg>4 Photos</span></div>
      <h3 class="name">CELINE</h3>
      <p class="desc">Art-Studentin: Liebe es mit meiner jugendlichen Frische, Fröhlichkeit und Lernlust dich aufzuheitern. Sich an mir zu laben ist ein Jungbrunnen für Geist und Körper. Wenn du dich dafür erkenntlich zeigst, würde dies mein Herz erwärmen. Wohne alleine und habe viel Zeit. Nun liegt es an dir den nächsten Schritt zu machen, meine Nummer hast du ja.</p>
      <div class="phone"><svg><use href="#tel"/></svg>0790001122</div>
    </article>
    <article class="card">
      <div class="photo" role="img" aria-label="Profilfoto von Marion" style="background:linear-gradient(#7a5a3c,#2e5a7a)"><span class="badge"><svg><use href="#cam"/></svg>4 Photos</span></div>
      <h3 class="name">MARION</h3>
      <p class="desc">Sehne mich nach einem Geniesser der alten Schule. Mag es wenn man mir die Türe öffnet. Ein Arrangement auf lange Zeit, etwas Liebe, Romanze und Aufregung. Ich bin ein easy going Mädchen mit viel Takt Gefühl und einem natürlichen Bedürfniss nach Erotik. Bist du der Mann meiner Sehnsucht? Lass es uns herausfinden!</p>
      <div class="phone"><svg><use href="#tel"/></svg>0790001122</div>
    </article>
    <article class="card">
      <div class="photo" role="img" aria-label="Profilfoto von Zoe" style="background:linear-gradient(#c8a870,#5a4a38)"><span class="badge"><svg><use href="#cam"/></svg>4 Photos</span></div>
      <h3 class="name">ZOE</h3>
      <p class="desc">Bin eine Balletttänzerin aus München und neu in der Schweiz, bin leider oft alleine und fühle mich einsam. Eine junge Frau sollte doch nicht einsam zuhause sitzen, oder! Bist du der Gentlemann, der mir die schönen Seiten des Lebens zeigt? Dann melde dich bitte! Im Gegenzug werde ich Dich dafür mit meiner Jugendlichkeit erfrischen. Bisou deine Zoe</p>
      <div class="phone"><svg><use href="#tel"/></svg>0790001122</div>
    </article>
  </div>

  <div class="col">
    <article class="card">
      <div class="photo" role="img" aria-label="Profilfoto von Emilia" style="background:linear-gradient(#a07a50,#4a3424)"><span class="badge"><svg><use href="#cam"/></svg>4 Photos</span></div>
      <h3 class="name">EMILIA</h3>
      <p class="desc">Suche den älteren charmanten Mann der die Frauen liebt: Junge Männer wissen einfach nicht wie man mich verwöhnt. Die wollen immer nur in den Ausgang, und nicht wie ich in Ausstellungen. Ich liebe ruhige, gemütliche Abende wo viel Zeit für gegenseitigen Genussvorhanden ist. freu mich auf dich.</p>
      <div class="phone"><svg><use href="#tel"/></svg>0790001122</div>
    </article>
    <article class="card">
      <div class="photo" role="img" aria-label="Profilfoto von Sara" style="background:linear-gradient(#d8c090,#5a4a3a)"><span class="badge"><svg><use href="#cam"/></svg>4 Photos</span></div>
      <h3 class="name">SARA</h3>
      <p class="desc">Jahre alt bist. Bist du wie ich auf der Suche nach einer lockeren Beziehung in welcher du deine Erfahrung an eine jüngere Frau weitergeben kannst, bei welcher beide Seiten Ihren Genuss daraus ziehen können und sich gleichzeitig keine Illusion über die Grenzen der Beziehung machen, dann bist du genau was ich suche. Wo wir uns für ein erstes kennen lernentreffen sollst du bestimmen. Um unser Treffen zu vereinbaren, schreib mir ein SMS. Küsse Sara</p>
      <div class="phone"><svg><use href="#tel"/></svg>0790001122</div>
    </article>
    <article class="card">
      <div class="photo" role="img" aria-label="Profilfoto von Zora" style="background:linear-gradient(#c8a070,#3a2a20)"><span class="badge"><svg><use href="#cam"/></svg>4 Photos</span></div>
      <h3 class="name">ZORA</h3>
      <p class="desc">Salut, ich bin eine herzliche und bodenständige Studentin mit einem Sexy Body. Sehne mich nach einem älteren Mann, an denn ich mich anlehnen kann. Dabei sollen unsere Treffen für beide von uns ein knisternde Abwechslung vom Alltag sein. Doch sollten uns die Grenzen unserer Beziehung bewusst sein. Ich suche keinen Verlobten und es ist gut wenn du auch nicht :). Freu mich wenn du dich meldest und wir uns auf ein Cüpli treffen. Kizzes Zora</p>
      <div class="phone"><svg><use href="#tel"/></svg>0790001122</div>
    </article>
  </div>
</main>

<footer class="footer">
  <nav><span>SEARCH</span><span>HELP</span><span>TERMS OF USE</span><span>PRIVACY POLICY</span></nav>
  <span class="copy">© All Right Reserved</span>
</footer>

</body>
</html>
```